Keystride Environmental and Regulatory - Summary of Services

Looking for a 3 (plus nice title page) brochure to advertise our various services for business (Keystride Environmental and Regulatory Inc) in the environmental and regulatory field for oil and gas clients based in Alberta Canada. We complete environmental assessments in the field to ensure the environment is protected, emissions modelling and carbon emissions modelling, along with managing regulatory requirements for oil and gas. I'm hoping to have various services and lists along with graphics that relate to that area. We want to cater towards a business that is strong, but has green ideals. I've attached the Land Renewal Initiative brochure as an example of services, as well as our original Keystride Brochure. I'd like to blend these two together for more of a modern feel with graphics overlay and condense to 3 pages (Title Page) for a more summary feel of this work.
Updates

Our website is Has lots of photos and the services on the website tab is what services we'd like to add to brochure. www.keystrideenvironmental.example

```html
<!DOCTYPE html>
<html lang="en">
<head>
<meta charset="utf-8">
<title>Keystride Environmental and Regulatory – About &amp; Values Spread</title>
<link href="https://fonts.googleapis.com/css2?family=Montserrat:ital,wght@0,300;0,400;0,500;0,600;0,700;0,800;1,800;1,900&display=swap" rel="stylesheet">
<style>
  :root {
    --navy: #233246;
    --navy-deep: #1b2839;
    --green: #8dc63f;
    --green-dark: #6fa82a;
    --paper: #ffffff;
    --ink: #2a3342;
    --line: #e8edf2;
    --backdrop: #e4e4e4;
  }
  * { box-sizing: border-box; margin: 0; padding: 0; }
  html, body { width: 1200px; height: 833px; overflow: hidden; background: var(--backdrop); }
  body { font-family: "Montserrat", sans-serif; color: var(--ink); }
  .spread { position: relative; width: 1200px; height: 833px; display: flex; }
  .page { position: relative; width: 600px; height: 833px; overflow: hidden; }

  /* Left page */
  .page--about { background: var(--paper); }
  .hero-photo { position: absolute; left: 0; top: 0; width: 600px; height: 260px;
    background: linear-gradient(180deg, #6d7a52 0%, #4e5b3a 45%, #3c4330 100%); }
  .about-band { position: absolute; left: 0; top: 200px; width: 600px; height: 120px; }
  .about-title { position: absolute; left: 0; top: 228px; width: 600px; text-align: center;
    color: #fff; font-size: 34px; letter-spacing: 1px; font-weight: 300; }
  .about-title strong { font-weight: 800; }
  .about-subtitle { position: absolute; left: 0; top: 300px; width: 600px; text-align: center;
    font-size: 16px; font-weight: 500; color: var(--navy); letter-spacing: .5px; }
  .about-subtitle span { color: var(--green); font-weight: 700; }
  .features { position: absolute; left: 30px; top: 335px; width: 540px; display: flex; }
  .feature { flex: 1; text-align: center; padding: 0 14px; }
  .feature + .feature { border-left: 1px solid #9aa3ad; }
  .feature svg { display: block; margin: 0 auto 10px; }
  .feature p { font-size: 9.5px; font-weight: 600; line-height: 1.35; color: var(--navy); }
  .intro-band { position: absolute; left: 0; top: 430px; width: 600px; height: 130px;
    background: var(--navy); clip-path: polygon(0 8%, 100% 0, 100% 100%, 0 100%); }
  .intro-text { position: absolute; left: 40px; top: 452px; width: 520px; text-align: center;
    color: #fff; font-size: 9.5px; line-height: 1.45; font-weight: 500; }
  .intro-text p + p { margin-top: 5px; }
  .team-title { position: absolute; left: 40px; top: 585px; color: var(--green);
    font-size: 30px; font-weight: 900; font-style: italic; line-height: 1.1; }
  .team-text { position: absolute; left: 40px; top: 668px; width: 320px;
    font-size: 9.5px; line-height: 1.4; font-weight: 500; color: var(--ink); }
  .team-text p + p { margin-top: 8px; }
  .team-photo { position: absolute; left: 400px; top: 570px; width: 170px; height: 190px;
    background: linear-gradient(160deg, #7f8e5c 0%, #5a6a3e 55%, #8b3a2e 100%); }

  /* Right page */
  .page--values { background: linear-gradient(180deg, #2b3a50 0%, var(--navy) 40%, var(--navy-deep) 100%); color: #fff; }
  .values-backdrop { position: absolute; inset: 0;
    background: radial-gradient(ellipse at 75% 30%, rgba(120,140,160,.18), transparent 60%),
                radial-gradient(ellipse at 40% 90%, rgba(90,105,125,.2), transparent 55%); }
  .values-title { position: absolute; left: 0; top: 52px; width: 600px; text-align: center;
    font-size: 36px; font-weight: 400; letter-spacing: 1px; }
  .values-title strong { font-weight: 800; }
  .title-rule { position: absolute; left: 180px; top: 98px; }

  .values-list { position: absolute; left: 50px; top: 122px; width: 500px;
    display: flex; flex-direction: column; gap: 14px; }
  .value { position: relative; padding: 36px 45px 30px 45px; }
  .value::before { content: ""; position: absolute; left: 4px; top: 16px; bottom: 36px; width: 6px;
    border-left: 1px solid var(--line); border-top: 1px solid var(--line); }
  .value::after { content: ""; position: absolute; right: 8px; top: 45%; bottom: 6px; width: 95px;
    border-right: 1px solid var(--line); border-bottom: 1px solid var(--line); }
  .value-quote { position: absolute; left: 13px; top: 0; font-size: 44px; font-weight: 800;
    line-height: 1; color: var(--green); height: 30px; overflow: hidden; }
  .value-rule { position: absolute; left: 42px; top: 12px; width: 50px; border-top: 1px solid var(--line); }
  .value h3 { font-size: 18px; font-weight: 700; color: var(--green); letter-spacing: .5px;
    line-height: 1.2; margin-bottom: 4px; }
  .value p { font-size: 11px; font-weight: 300; line-height: 1.38; text-align: justify; color: var(--line); }
  .value--mission p { text-align: left; }

  .brand-name { position: absolute; right: 50px; top: 735px; font-size: 34px; font-weight: 600;
    letter-spacing: 3px; color: #fff; }
</style>
</head>
<body>
<main class="spread">
  <!-- Left page: about -->
  <section class="page page--about">
    <div class="hero-photo" role="img" aria-label="Field crew in hard hats and work wear seated on a log in a forest"></div>
    <svg class="about-band" width="600" height="120" viewBox="0 0 600 120" aria-hidden="true">
      <defs>
        <linearGradient id="bandGreen" x1="0" x2="0" y1="0" y2="1">
          <stop offset="0" stop-color="#8dc63f" stop-opacity="0"/>
          <stop offset=".35" stop-color="#8dc63f" stop-opacity=".85"/>
          <stop offset="1" stop-color="#6fa82a"/>
        </linearGradient>
      </defs>
      <path d="M0 20 Q300 -10 600 30 L600 95 Q300 60 0 95 Z" fill="url(#bandGreen)"/>
      <path d="M0 95 Q300 60 600 95 L600 120 L0 120 Z" fill="#fff"/>
    </svg>
    <h1 class="about-title">EVERYTHING <strong>ABOUT US</strong></h1>
    <h2 class="about-subtitle">ITS LL ABOUT PROTECTING <span>THE ENVIROMENT</span></h2>

    <div class="features">
      <div class="feature">
        <svg width="46" height="46" viewBox="0 0 46 46" aria-hidden="true">
          <circle cx="23" cy="23" r="23" fill="var(--green)"/>
          <path d="M11 24 L18 18 L24 21 L30 17 L35 23 L26 31 L20 29 Z" fill="none" stroke="#fff" stroke-width="2" stroke-linejoin="round"/>
        </svg>
        <p>Lorem ipsum dolor sit amet, consectetuer adipiscing elit.</p>
      </div>
      <div class="feature">
        <svg width="46" height="46" viewBox="0 0 46 46" aria-hidden="true">
          <circle cx="23" cy="23" r="23" fill="var(--navy)"/>
          <circle cx="23" cy="23" r="12" fill="none" stroke="#fff" stroke-width="2"/>
          <circle cx="23" cy="23" r="7" fill="none" stroke="#fff" stroke-width="2"/>
          <circle cx="23" cy="23" r="2.5" fill="#fff"/>
          <path d="M23 23 L34 12" stroke="#fff" stroke-width="2"/>
        </svg>
        <p>Lorem ipsum dolor sit amet, consectetuer.</p>
      </div>
      <div class="feature">
        <svg width="46" height="46" viewBox="0 0 46 46" aria-hidden="true">
          <circle cx="23" cy="23" r="23" fill="var(--green)"/>
          <path d="M14 24 L20 30 L33 16" fill="none" stroke="#fff" stroke-width="3" stroke-linecap="round" stroke-linejoin="round"/>
        </svg>
        <p>Lorem ipsum dolor sit amet, consectetuer adipiscing elit.</p>
      </div>
    </div>

    <div class="intro-band"></div>
    <div class="intro-text">
      <p>Keystride Environmental &amp; Regulatory (Keystride) is a dynamic and agile environmental consulting group.</p>
      <p>Incorporated in 2014, Keystride provides cost-effective environmental and regulatory consulting for the energy industry, commercial, and municipal Clients in Alberta, British Columbia, and Saskatchewan. We gained a strong reputation for our responsive, practical, and efficient solutions to all environmental and regulatory challenges faced by our Customers.</p>
    </div>

    <h2 class="team-title">OUR EXEPTIONAL<br>TEAM</h2>
    <div class="team-text">
      <p>Our high-performance team of thoroughly chosen professionals with proven expertise in soil, water, wildlife, and vegetation assessments, contamination management and remediation, spill response, regulatory approvals, and regulatory closure is our biggest strength.</p>
      <p>Since the inception of Keystride in 2014, our team has successfully completed a truly wide range of exciting projects for our Clients. We incorporate creativity, practicality, and problem-solving into all our projects</p>
    </div>
    <div class="team-photo" role="img" aria-label="Crew member in safety vest riding a quad through a forest creek"></div>
  </section>

  <!-- Right page: values -->
  <section class="page page--values">
    <div class="values-backdrop" role="img" aria-label="Faint mountain landscape with a truck on the road"></div>
    <h2 class="values-title">OUR <strong>VALUES</strong></h2>
    <svg class="title-rule" width="240" height="16" viewBox="0 0 240 16" aria-hidden="true">
      <line x1="0" y1="6" x2="240" y2="10" stroke="#fff" stroke-width="1"/>
      <path d="M105 12 Q115 2 125 8 Q132 12 138 4" fill="none" stroke="var(--green)" stroke-width="4" stroke-linecap="round"/>
    </svg>

    <div class="values-list">
      <article class="value value--mission">
        <span class="value-quote" aria-hidden="true">“</span>
        <span class="value-rule" aria-hidden="true"></span>
        <h3>OUR MISSION IS SIMPLE.</h3>
        <p>To serve our clients.<br>To provide expert and innovative consulting.<br>To deliver cost efficient environmental and regulatory solutions.</p>
      </article>

      <article class="value value--clients">
        <span class="value-quote" aria-hidden="true">“</span>
        <span class="value-rule" aria-hidden="true"></span>
        <h3>OUR CLIENTS ARE PHENOMENAL.</h3>
        <p>Client relationships are the foundation of our group. We build our business on our clients’ success. Keystride prides itself for its ability to listen to our clients’ needs, understand their issues, and present viable solutions.</p>
      </article>

      <article class="value value--results">
        <span class="value-quote" aria-hidden="true">“</span>
        <span class="value-rule" aria-hidden="true"></span>
        <h3>OUR RESULTS ARE REMARKABLE.</h3>
        <p>We routinely develop and apply the site-specific environmental guideline values that are defensible, more suitable, and less stringent compared to the generic Tier 1 “one-fits-all” approach that is often unnecessarily restrictive. Our subject matter experts skillfully use all tools available in the environmental regulations including Tier 2 guidelines, statistical calculations, subsoil values for salinity and hydrocarbons, as well as guidelines for remote sites. Thinking outside the box is our standard approach...it makes sense!</p>
      </article>
    </div>

    <div class="brand-name">KEYSTRIDE</div>
  </section>
</main>
</body>
</html>
```